Digital Album Cover - Frosted Lanterns (Night Falls Still)

HiI need a digital album cover for a piano instrumental cover single

Artist: Corey Dalton
Title: Frosted Lanterns (Night Falls Still)

The song was originally by Derek Holloway

Please use my logo

You can listen to the track herehttps://soundcloud.com/coreydaltonkeys/frosted-lanterns-night-falls-still-piano-instrumental-cover

Requirements
Must have
• My logo design Corey Dalton

```html
<!DOCTYPE html>
<html lang="en">
<head>
<meta charset="utf-8">
<title>Corey Dalton – Frosted Lanterns (Night Falls Still)</title>
<link rel="stylesheet" href="https://fonts.googleapis.com/css2?family=Arimo:wght@400;700&family=Great+Vibes&family=Open+Sans:wght@400;600&display=swap">
<style>
  :root {
    --ink: #000000;
    --paper: #ffffff;
    --glow-core: #8a3c0c;
    --glow-mid: #4a1d06;
    --glow-edge: #120603;
    --key-light: #f4f4f4;
    --key-shade: #bdbdbd;
    --key-dark: #1a1a1a;
  }
  html, body {
    margin: 0;
    padding: 0;
    width: 1200px;
    height: 1200px;
    overflow: hidden;
    background: var(--ink);
  }
  .cover {
    position: relative;
    width: 1200px;
    height: 1200px;
    overflow: hidden;
    background: var(--ink);
  }
  .sparkle-glow {
    position: absolute;
    left: -80px;
    top: 220px;
    width: 900px;
    height: 800px;
    background:
      radial-gradient(ellipse 48% 30% at 42% 48%, rgba(176, 84, 22, 0.75) 0%, rgba(120, 50, 12, 0.5) 40%, rgba(40, 14, 4, 0) 100%),
      radial-gradient(ellipse 60% 50% at 30% 60%, var(--glow-mid) 0%, var(--glow-edge) 60%, rgba(0,0,0,0) 100%);
  }
  .keyboard {
    position: absolute;
    inset: 0;
    width: 1200px;
    height: 1200px;
  }
  .artist {
    position: absolute;
    left: 103px;
    top: 290px;
    margin: 0;
    font-family: "Arimo", Arial, sans-serif;
    font-weight: 700;
    font-size: 44px;
    letter-spacing: 0.5px;
    color: var(--paper);
  }
  .title {
    position: absolute;
    left: 95px;
    top: 385px;
    margin: 0;
    font-family: "Great Vibes", cursive;
    font-weight: 400;
    font-size: 108px;
    line-height: 1;
    color: var(--paper);
    white-space: nowrap;
  }
  .subtitle {
    position: absolute;
    right: 437px;
    top: 596px;
    margin: 0;
    font-family: "Open Sans", Arial, sans-serif;
    font-size: 33px;
    color: var(--paper);
    white-space: nowrap;
  }
  .brand {
    position: absolute;
    left: 38px;
    top: 1038px;
    display: flex;
    align-items: center;
    gap: 16px;
  }
  .brand-mark {
    width: 98px;
    height: 98px;
    border-radius: 50%;
    background: var(--paper);
    flex: none;
  }
  .brand-text {
    display: flex;
    flex-direction: column;
    align-items: center;
  }
  .brand-name {
    font-family: "Arimo", Arial, sans-serif;
    font-weight: 400;
    font-size: 36px;
    line-height: 1;
    color: var(--paper);
    letter-spacing: 0.5px;
  }
  .brand-tagline {
    margin-top: 8px;
    font-family: "Open Sans", Arial, sans-serif;
    font-size: 15px;
    color: var(--paper);
  }
</style>
</head>
<body>
<main class="cover">
  <div class="sparkle-glow" role="img" aria-label="Warm golden bokeh sparkles glowing on a dark background"></div>

  <svg class="keyboard" viewBox="0 0 1200 1200" role="img" aria-label="Curved piano keyboard sweeping down the right side">
    <defs>
      <linearGradient id="keyboard-tone" x1="0" y1="0" x2="1" y2="0">
        <stop offset="0" stop-color="var(--key-light)"/>
        <stop offset="0.55" stop-color="var(--key-shade)"/>
        <stop offset="1" stop-color="var(--key-dark)"/>
      </linearGradient>
    </defs>
    <path d="M1093 0 C1020 240 930 420 790 590 C640 770 510 960 405 1200 L760 1200 C870 980 1000 790 1140 610 C1190 545 1200 520 1200 510 L1200 0 Z" fill="url(#keyboard-tone)"/>
  </svg>

  <h2 class="artist">COREY DALTON</h2>
  <h1 class="title">Frosted Lanterns</h1>
  <p class="subtitle">(Night Falls Still)</p>

  <div class="brand">
    <div class="brand-mark"></div>
    <div class="brand-text">
      <span class="brand-name">COREY DALTON</span>
      <span class="brand-tagline">Wedding &amp; Event Pianist</span>
    </div>
  </div>
</main>
</body>
</html>
```